Touring Cabaret Seasons Needs a Poster Design

We need a poster design for upcoming Cabaret seasons in Melbourne and Adelaide (Australia) for a prestigious festival.

Show is titled "Here's a Small Thing I Dreamed Up Last Week..." and is a comedy parody of bad cabaret and deluded performers. We'd like the poster to reflect the comedy of the piece without being silly and inaccessable.

Artist has recently won awards for this show and these will need to be listed as a part of the design.

I have attached a couple of photographs that can be used - one is the artist with a blank book cover and these could be used to overlay text.

Would like it to not look too wordy, however I realise we've asked for a lot of text to be included.

Target Market(s)

Ages 20 - 40 cabaret or comedy fans.

Industry/Entity Type

Festival

Requirements
Must have
• TEXT:
The Velvet Parlour presents:
Here's a Small Thing I Dreamed Up Last Week...

TEXT:
WINNER of BEST CABARET, BEST WRITING and PEOPLE’S CHOICE awards at Quick + Tidy Revue 2011

TEXT:
The Lantern Room (Melbourne)
Feb 23rd to the 26th

Le Corbeau, REVedge(Adelaide)
March 3rd and 4th

QUOTES:
“...the funniest things in spandex. 4.5 stars” – The Courier Post on Rally! A revue about lawn bowls.

“a clever dissection of bad cabaret” – Owen Blackwood, The Courier Post on Quick + Tidy Revue
Nice to have
• TEXT:
The last time someone showed you a little something they were working on, did you lose an hour of your life you will never get back? Don’t worry – we’ve all been there.

TEXT:
Composer and co-writer of Rally! (A revue about lawn bowls) and WINNER of BEST CABARET, BEST WRITING and PEOPLE’S CHOICE awards at Quick + Tidy Revue 2011, presents her full show, with more original music and helpful anecdotes.

WEBSITE:
More info at www.mingleface.example/thevelvetparlour

```html
<!DOCTYPE html>
<html lang="en">
<head>
<meta charset="utf-8">
<title>Here's a Small Thing I Dreamed Up Last Week... – The Velvet Parlour</title>
<link rel="stylesheet" href="https://fonts.googleapis.com/css2?family=Alfa+Slab+One&family=Annie+Use+Your+Telescope&display=swap">
<style>
  :root {
    --page: #ffffff;
    --poster: #000000;
    --magenta: #b8177b;
    --chalk: #f2f2f2;
    --bubble: #3a3a3c;
    --bubble-shade: #1e1e1f;
    --blue: #3d84c6;
    --gold: #b59a2a;
    --hair: #c9a878;
    --skin: #e7c3ae;
  }
  * { margin: 0; padding: 0; box-sizing: border-box; }
  html, body { width: 1200px; height: 800px; overflow: hidden; background: var(--page); }
  .canvas { position: relative; width: 1200px; height: 800px; background: var(--page); }
  .poster {
    position: absolute; left: 323px; top: 0; width: 555px; height: 800px;
    background: var(--poster); overflow: hidden;
    font-family: "Annie Use Your Telescope", cursive; color: var(--chalk);
  }
  .shapes { position: absolute; inset: 0; width: 555px; height: 800px; }
  .presenter { position: absolute; top: 40px; width: 100%; text-align: center; font-size: 20px; letter-spacing: .3px; }
  .title {
    position: absolute; top: 80px; width: 100%; text-align: center;
    font-family: "Alfa Slab One", serif; font-weight: 400; color: var(--magenta);
    font-size: 30px; line-height: 38px; letter-spacing: 1.5px; text-transform: uppercase;
  }
  .awards { position: absolute; top: 176px; width: 100%; text-align: center; font-size: 13px; white-space: nowrap; }
  .teaser {
    position: absolute; left: 34px; top: 240px; width: 238px;
    color: var(--magenta); font-size: 14px; line-height: 16px; text-align: center;
  }
  .venue { position: absolute; color: var(--blue); text-align: center; font-size: 16px; line-height: 19px; }
  .venue--adelaide { left: 300px; top: 401px; width: 200px; }
  .venue--melbourne { left: 300px; top: 505px; width: 215px; }
  .illustration { position: absolute; }
  .illustration--winged-pencil { left: 300px; top: 222px; width: 196px; height: 120px;
    background: linear-gradient(135deg, #5a4c1a 0%, #1d3a52 60%, #0d0d0d 100%); border-radius: 40px 60px 20px 30px; }
  .illustration--crown { left: 114px; top: 424px; width: 70px; height: 58px;
    background: linear-gradient(180deg, var(--gold), #6c5a18); border-radius: 8px; }
  .illustration--turtle { left: 490px; top: 655px; width: 34px; height: 90px;
    background: linear-gradient(180deg, #7c8d3a, #3a4418); border-radius: 16px; }
  .photo { position: absolute; left: 77px; top: 488px; width: 200px; height: 170px;
    background: linear-gradient(180deg, var(--hair) 0%, #d9b58f 35%, var(--skin) 62%, #c9a08a 100%); }
  .quote { position: absolute; right: 80px; text-align: right; white-space: nowrap; }
  .quote__text { display: block; font-size: 18px; line-height: 20px; }
  .quote__credit { display: block; font-size: 12px; line-height: 15px; }
  .quote--spandex { top: 660px; }
  .quote--dissection { top: 704px; }
  .website { position: absolute; top: 756px; width: 100%; text-align: center; color: var(--magenta); font-size: 21px; white-space: nowrap; }
</style>
</head>
<body>
<div class="canvas">
  <div class="poster">
    <svg class="shapes" viewBox="0 0 555 800" aria-hidden="true">
      <g stroke="var(--chalk)" stroke-width="1.5" stroke-linejoin="round">
        <rect x="27" y="235" width="263" height="97" rx="24" fill="var(--bubble-shade)"/>
        <path d="M83,332 L83,381 Q83,396 98,396 L206,396 L206,426 L186,426 L227,471 L268,426 L246,426 L246,371 L103,371 L103,332 Z" fill="var(--bubble-shade)"/>
        <rect x="21" y="229" width="263" height="97" rx="24" fill="var(--bubble)"/>
        <path d="M77,326 L77,375 Q77,390 92,390 L200,390 L200,420 L180,420 L221,465 L262,420 L240,420 L240,365 L97,365 L97,326 Z" fill="var(--bubble)"/>
        <path d="M303,399 h195 a14,14 0 0 1 14,14 v54 a14,14 0 0 1 -14,14 h-170 l-22,22 l4,-22 a14,14 0 0 1 -7,-12 v-56 a14,14 0 0 1 14,-14 z" fill="var(--bubble-shade)"/>
        <path d="M297,393 h195 a14,14 0 0 1 14,14 v54 a14,14 0 0 1 -14,14 h-170 l-22,22 l4,-22 a14,14 0 0 1 -7,-12 v-56 a14,14 0 0 1 14,-14 z" fill="var(--bubble)"/>
        <path d="M303,497 h208 a16,16 0 0 1 16,16 v68 a16,16 0 0 1 -16,16 h-180 l-26,24 l6,-24 a16,16 0 0 1 -8,-14 v-70 a16,16 0 0 1 16,-16 z" fill="var(--bubble-shade)"/>
        <path d="M297,491 h208 a16,16 0 0 1 16,16 v68 a16,16 0 0 1 -16,16 h-180 l-26,24 l6,-24 a16,16 0 0 1 -8,-14 v-70 a16,16 0 0 1 16,-16 z" fill="var(--bubble)"/>
      </g>
    </svg>

    <p class="presenter">The Velvet Parlour presents:</p>
    <h1 class="title">Here's a Small Thing<br>I Dreamed Up Last Week...</h1>
    <p class="awards">WINNER of BEST CABARET, BEST WRITING and PEOPLE’S CHOICE awards at Quick + Tidy Revue 2011</p>

    <p class="teaser">The last time someone showed you a little something they were working on, did you lose an hour of your life you will never get back? Don’t worry – we’ve all been there.</p>

    <div class="illustration illustration--winged-pencil" role="img" aria-label="Sketched pencil with golden wings"></div>

    <p class="venue venue--adelaide">Le Corbeau, REVedge<br>(Adelaide)<br>March 3rd and 4th</p>
    <p class="venue venue--melbourne">The Lantern Room<br>(Melbourne)<br>Feb 23rd to the 26th</p>

    <div class="photo" role="img" aria-label="Photograph of the performer, cropped at the eyes"></div>
    <div class="illustration illustration--crown" role="img" aria-label="Sketched gold crown above the performer"></div>
    <svg class="shapes" viewBox="0 0 555 800" aria-hidden="true">
      <path d="M70,650 L95,646 L110,652 L128,645 L150,651 L168,644 L190,650 L212,645 L232,652 L255,646 L284,650 L284,662 L70,662 Z" fill="var(--chalk)"/>
      <path d="M60,655 L90,652 L120,658 L150,654 L180,659 L220,653 L260,658 L300,654 L300,672 L60,672 Z" fill="var(--poster)"/>
    </svg>

    <p class="quote quote--spandex">
      <span class="quote__text">“...the funniest things in spandex. 4.5 stars”</span>
      <span class="quote__credit">The Courier Post on Rally! A revue about lawn bowls.</span>
    </p>
    <p class="quote quote--dissection">
      <span class="quote__text">“a clever dissection of bad cabaret”</span>
      <span class="quote__credit">Owen Blackwood, The Courier Post on Quick + Tidy Revue</span>
    </p>
    <div class="illustration illustration--turtle" role="img" aria-label="Small sketched tortoise doodle"></div>

    <p class="website">More info at www.mingleface.example/thevelvetparlour</p>
  </div>
</div>
</body>
</html>
```